Thornfield Marsh, LLC Website

We are a small law firm in need of a website that contains the following:
1. Attractive main page
2. About us/attorney info for three people: Leonard Thornfield (attorney), Brent Marsh (attorney), and Melinda Carrow (legal assistant). We have bio's ready to submit.
3. Blog/video page. We'd like to post blogs and videos to help drive traffic
4. Multidistrict Litigation and Class Actions page, where we post information regarding active MDLs and Class actions that we are doing intake on.
Updates

Can you also please use the color "gold" in the design and logo? Thanks.

Industry/Entity Type

Legal

Coding

Coded - Design and coding required

Number of Pages Required

1 page

Colors
0054AA
0677BA
7BADD7
CADEEF
E8F1F8

Requirements
Must have
• 1. Attractive main page 2. About us/attorney info for three people: Leonard Thornfield (attorney), Brent Marsh (attorney), and Melinda Carrow (legal assistant). We have bio's ready to submit. 3. Blog/video page. We'd like to post blogs and videos to help drive traffic 4. Multidistrict Litigation and Class Actions page, where we post information regarding active MDLs and Class actions that we are doing intake on.

```html
<!DOCTYPE html>
<html lang="en">
<head>
<meta charset="utf-8">
<title>Thornfield Marsh, LLC – Lawyers</title>
<link href="https://fonts.googleapis.com/css2?family=Montserrat:wght@300;400;500;600;700&family=Lato:wght@400;700&display=swap" rel="stylesheet">
<style>
:root{
  --stage:#b3b3b3;
  --sky:#1fb5fa;
  --navy:#0c1f77;
  --navy-title:#1b2a86;
  --ink:#222;
  --body:#444;
  --muted:#777;
  --soft:#f6f6f6;
  --footer:#000;
  --gold:#d9a441;
  --white:#fff;
}
*{margin:0;padding:0;box-sizing:border-box}
html,body{width:1200px;height:1200px;overflow:hidden;background:var(--stage)}
.stage{position:absolute;left:0;top:0;width:1932px;height:1932px;transform:scale(.62112);transform-origin:0 0;font-family:"Lato",sans-serif}
.page{position:absolute;left:672px;top:10px;width:616px;height:1903px;background:var(--white);overflow:hidden}
.abs{position:absolute}

/* top bar */
.topbar{left:0;top:0;width:616px;height:17px;background:var(--sky)}
.topbar .addr{left:47px;top:4px;font-size:6px;color:var(--white);display:flex;align-items:center;gap:3px}
.topbar .social{right:42px;top:3px;display:flex;gap:3px}
.topbar .social span{width:11px;height:11px;border:1.5px solid var(--white);border-radius:2px}

/* header */
.header{left:0;top:17px;width:616px;height:40px;background:var(--white);border-bottom:1px solid #ddd}
.logo{left:47px;top:12px;display:flex;align-items:center;gap:4px}
.logo .mark{width:16px;height:16px;background:var(--navy)}
.logo .name{font-family:"Montserrat",sans-serif;font-weight:600;font-size:8.5px;color:var(--navy)}
.nav{left:223px;top:19px;display:flex;gap:8px;font-family:"Lato",sans-serif;font-weight:700;font-size:6.3px;color:var(--navy)}
.nav .sep{color:#333;font-weight:400}
.cta-btn{left:481px;top:16px;width:94px;height:16px;background:var(--navy);border-radius:2px;color:var(--white);font-weight:700;font-size:6px;display:flex;align-items:center;justify-content:center}

/* hero */
.hero{left:0;top:57px;width:616px;height:281px;background:linear-gradient(100deg,#2b2620 0%,#6b5238 30%,#3a3128 55%,#8a7358 75%,#2f2a25 100%)}
.hero-box{left:47px;top:70px;width:236px;height:142px;background:linear-gradient(160deg,#1233b0,#0b2290);text-align:center;color:var(--white)}
.hero-box h1{font-family:"Montserrat",sans-serif;font-weight:700;font-size:20px;line-height:24px;margin-top:21px}
.hero-box p{font-size:8.5px;margin-top:5px}
.hero-box .btn{display:inline-flex;margin-top:9px;width:69px;height:19px;background:var(--white);color:var(--navy);border-radius:2px;font-size:6.5px;align-items:center;justify-content:center}

/* section titles */
.sec-title{left:0;width:616px;text-align:center;font-family:"Montserrat",sans-serif;font-weight:300;color:var(--ink)}
.rule{left:281px;width:53px;height:2px;background:var(--sky)}
.lead{left:57px;width:502px;text-align:center;font-family:"Montserrat",sans-serif;font-size:6.4px;line-height:10px;color:var(--body)}

/* experts */
.photo{width:302px;height:194px}
.expert h2{font-family:"Montserrat",sans-serif;font-weight:600;font-size:11.5px;color:var(--navy-title)}
.expert p{margin-top:7px;width:246px;font-size:5.8px;line-height:9.6px;color:var(--ink)}
.expert .btn{margin-top:18px;width:69px;height:19px;background:var(--navy);border-radius:2px;color:var(--white);font-size:6.5px;display:flex;align-items:center;justify-content:center}

/* litigation */
.soft{left:0;top:1214px;width:616px;height:333px;background:var(--soft)}
.card{width:167px}
.card .img{height:119px}
.card .meta{height:22px;display:flex;align-items:center;font-size:5.5px;color:var(--muted)}
.card .date{width:56px;height:22px;background:var(--sky);color:var(--white);display:flex;align-items:center;padding-left:6px}
.card .meta .by{margin-left:14px}
.card .meta .cm{margin-left:22px}
.card h3{font-family:"Montserrat",sans-serif;font-weight:400;font-size:10.5px;color:var(--ink);margin-top:10px}
.card p{font-family:"Montserrat",sans-serif;font-size:6px;line-height:11px;color:var(--muted);margin-top:4px}

/* call to action */
.band{left:0;top:1547px;width:616px;height:110px;background:var(--sky);text-align:center;color:var(--white)}
.band h2{font-family:"Montserrat",sans-serif;font-weight:400;font-size:12.5px;margin-top:31px}
.band h2 b{font-weight:700}
.band .btn{display:inline-flex;margin-top:12px;width:132px;height:21px;border:1.5px solid var(--white);border-radius:2px;font-size:8px;align-items:center;justify-content:center}

/* footer */
.footer{left:0;top:1657px;width:616px;height:246px;background:var(--footer);color:var(--white)}
.fcol{top:46px}
.fcol h4{font-family:"Montserrat",sans-serif;font-weight:600;font-size:8.5px}
.fcol .bar{width:22px;height:2px;background:var(--sky);margin-top:8px}
.fabout p{font-size:6.2px;line-height:11px;color:var(--gold);width:118px;margin-top:9px}
.fsocial{display:flex;gap:6px;margin-top:10px}
.fsocial span{width:16px;height:16px;border:1.2px solid var(--sky)}
.flist{list-style:none;margin-top:10px}
.flist li{font-size:6px;height:15.5px;display:flex;align-items:center;gap:5px}
.flist li::before{content:"";width:3px;height:3px;border-radius:50%;background:var(--sky)}
.fcontact div{font-size:6px;height:18px;display:flex;align-items:center;gap:5px}
.fcontact div:first-of-type{margin-top:14px}
.thumbs{display:grid;grid-template-columns:repeat(3,37px);gap:3px;margin-top:11px}
.thumbs span{height:26px}
.t1{background:linear-gradient(135deg,#3a2a1c,#c7a27a)}
.t2{background:linear-gradient(135deg,#8a4a30,#d9b089)}
.t3{background:linear-gradient(135deg,#bdbdbd,#6f6f6f)}
.totop{left:562px;top:208px;width:13px;height:13px;background:var(--white)}
.fline{left:0;top:214px;width:616px;height:1px;background:#333}
.copy{left:0;top:228px;width:616px;text-align:center;font-size:6.2px}
</style>
</head>
<body>
<div class="stage">
<div class="page">

  <div class="abs topbar">
    <div class="abs addr">
      <svg width="6" height="8" viewBox="0 0 6 8"><path d="M3 0a3 3 0 0 0-3 3c0 2 3 5 3 5s3-3 3-5a3 3 0 0 0-3-3z" fill="#fff"/><circle cx="3" cy="3" r="1" fill="#1fb5fa"/></svg>
      42 Larkspur Avenue, Redmont Bay ZIP 550 210
    </div>
    <div class="abs social"><span></span><span></span><span></span></div>
  </div>

  <header class="abs header">
    <div class="abs logo"><span class="mark"></span><span class="name">THORNFIELD MARSH, LLC</span></div>
    <nav class="abs nav">
      <span>HOME PAGE</span><span class="sep">|</span><span>ABOUT US</span><span class="sep">|</span><span>BLOG</span><span class="sep">|</span><span>VIDEO PAGE</span><span class="sep">|</span><span>CONTACT US</span>
    </nav>
    <div class="abs cta-btn">GET FREE CONSULTATION</div>
  </header>

  <section class="abs hero" role="img" aria-label="Bronze statue of Lady Justice with scales in front of a blurred law library">
    <div class="abs hero-box">
      <h1>WE ARE VOICE<br>OF JUSTICE</h1>
      <p>Lowyer / Law Firm / Attorney</p>
      <span class="btn">READ MORE</span>
    </div>
  </section>

  <h2 class="abs sec-title" style="top:364px;font-size:19px">ABOUT US</h2>
  <div class="abs rule" style="top:399px"></div>
  <p class="abs lead" style="top:421px">Lorem Ipsum is simply dummy text of the printing and typesetting industry. Lorem Ipsum has been the industry's standard dummy text ever since the 1500s, when an unknown printer took a galley of type and scrambled it to make a type specimen book. It has survived not only five centuries, but also the leap into electronic typesetting, remaining essentially unchanged. It was popularised in the 1960s with the release of Typeleaf sheets containing Lorem Ipsum passages, and more recently with desktop publishing software like Quillset Layout including versions of Lorem Ipsum.</p>

  <h2 class="abs sec-title" style="top:493px;font-size:19px">WE ARE LAWYER EXPERTS</h2>
  <div class="abs rule" style="top:528px"></div>

  <div class="abs photo" style="left:0;top:560px;background:linear-gradient(120deg,#5c5c5c,#2a2a2a 45%,#cfcfcf 85%)" role="img" aria-label="Portrait of Leonard Thornfield, smiling attorney in a dark suit"></div>
  <div class="abs expert" style="left:327px;top:583px">
    <h2>LEONARD THORNFIELD</h2>
    <p>There are many variations of passages of Lorem Ipsum available, but the majority have suffered alteration in some form, by injected humour, or randomised words which don't look even slightly believable. If you are going to use a passage of Lorem Ipsum, you need to be sure there isn't anything embarrassing hidden in the middle of text. All the Lorem Ipsum generators on the Internet tend to repeat predefined chunks as necessary, making this the first true generator on the Internet. It uses a dictionary of over 200 Latin words, combined with a handful of model sentence structures, to generate Lorem Ipsum which looks reasonable.</p>
    <div class="btn">READ MORE</div>
  </div>

  <div class="abs expert" style="left:47px;top:816px">
    <h2>BRENT MARSH</h2>
    <p>There are many variations of passages of Lorem Ipsum available, but the majority have suffered alteration in some form, by injected humour, or randomised words which don't look even slightly believable. If you are going to use a passage of Lorem Ipsum, you need to be sure there isn't anything embarrassing hidden in the middle of text. All the Lorem Ipsum generators on the Internet tend to repeat predefined chunks as necessary, making this the first true generator on the Internet. It uses a dictionary of over 200 Latin words, combined with a handful of model sentence structures, to generate Lorem Ipsum which looks reasonable.</p>
    <div class="btn" style="margin-left:-1px">READ MORE</div>
  </div>
  <div class="abs photo" style="left:314px;top:777px;background:linear-gradient(90deg,#8e8a85,#b3aea8 50%,#6f6b66)" role="img" aria-label="Portrait of Brent Marsh, attorney in a navy suit against a stone wall"></div>

  <div class="abs photo" style="left:0;top:991px;background:linear-gradient(120deg,#e9e4dc,#b9b1a5 45%,#2a2c33 70%,#d6d0c6)" role="img" aria-label="Melinda Carrow's photo: a professional writing notes at a desk with coffee"></div>
  <div class="abs expert" style="left:327px;top:1014px">
    <h2>MELINDA CARROW</h2>
    <p>There are many variations of passages of Lorem Ipsum available, but the majority have suffered alteration in some form, by injected humour, or randomised words which don't look even slightly believable. If you are going to use a passage of Lorem Ipsum, you need to be sure there isn't anything embarrassing hidden in the middle of text. All the Lorem Ipsum generators on the Internet tend to repeat predefined chunks as necessary, making this the first true generator on the Internet. It uses a dictionary of over 200 Latin words, combined with a handful of model sentence structures, to generate Lorem Ipsum which looks reasonable.</p>
    <div class="btn">READ MORE</div>
  </div>

  <section class="abs soft">
    <h2 class="abs sec-title" style="top:24px;font-size:15px;font-weight:400">MULTIDISTRICT LITIGATION AND CLASS</h2>
    <div class="abs rule" style="top:52px"></div>
    <p class="abs lead" style="top:68px;left:90px;width:440px;font-size:6.3px;line-height:11px;color:var(--muted)">Lorem ipsum dolor sit amet, consectetur adipisicing elit. Obcaecati laborum ipsa, a voluptates libero possimus sapiente sint odit iusto blanditiis doloribus.</p>

    <article class="abs card" style="left:47px;top:102px">
      <div class="img" style="background:linear-gradient(120deg,#6b4a22,#2b2b30 45%,#e6e3de 75%)" role="img" aria-label="Lawyer signing documents at a desk"></div>
      <div class="meta"><span class="date">Mar, 13 2025</span><span class="by">by admin</span><span class="cm">02</span></div>
      <h3>The Bond Market Is</h3>
      <p>Lorem ipsum dolor sit amet, consectetur adipisicing elit. Autem earum, laborum. Commodi nostrum culpa maxime provident quisquam, praesentium.......</p>
    </article>
    <article class="abs card" style="left:227px;top:102px">
      <div class="img" style="background:linear-gradient(160deg,#d9a07a,#8a4a2e 55%,#5a2e1e)" role="img" aria-label="Brass scales of justice in a courtroom"></div>
      <div class="meta"><span class="date">Mar, 13 2025</span><span class="by">by admin</span><span class="cm">02</span></div>
      <h3>Going To Get Ugly ITher Isn't</h3>
      <p>Lorem ipsum dolor sit amet, consectetur adipisicing elit. Autem earum, laborum. Commodi nostrum culpa maxime provident quisquam, praesentium.......</p>
    </article>
    <article class="abs card" style="left:407px;top:102px">
      <div class="img" style="background:linear-gradient(90deg,#cfcfcf,#8d8d8d 40%,#e2e2e2 70%,#9a9a9a)" role="img" aria-label="Stone columns of a courthouse"></div>
      <div class="meta"><span class="date">Mar, 13 2025</span><span class="by">by admin</span><span class="cm">02</span></div>
      <h3>To Get Ugly IThe Rebound Soon</h3>
      <p>Lorem ipsum dolor sit amet, consectetur adipisicing elit. Autem earum, laborum. Commodi nostrum culpa maxime provident quisquam, praesentium.......</p>
    </article>
  </section>

  <section class="abs band">
    <h2>IF YOU HAVE ANY <b>LEGAL PROBLEM</b> IN <b>YOUR LIFE</b> ... <b>WE ARE AVAILABLE</b></h2>
    <span class="btn">GET FREE CONSULTATION</span>
  </section>

  <footer class="abs footer">
    <div class="abs fcol fabout" style="left:48px">
      <h4>ABOUT US</h4><div class="bar"></div>
      <p>Thereare aswrta serttrmany variations of passages of Lorem Ipsum available, but the majority have suffered setyu..</p>
      <p style="margin-top:9px">Thereare aswrta serttrmany variations of passages of Lorem Ipsum available.</p>
      <div class="fsocial"><span></span><span></span><span></span><span></span></div>
    </div>
    <div class="abs fcol" style="left:181px">
      <h4>EXPLORE OUR WORK</h4><div class="bar"></div>
      <ul class="flist"><li>Criminal law</li><li>Accident law</li><li>Devorce law</li><li>Industrial law</li><li>Business law</li><li>Familly law</li></ul>
    </div>
    <div class="abs fcol fcontact" style="left:315px">
      <h4>KEEP IN TOUCH</h4><div class="bar"></div>
      <div><svg width="7" height="7" viewBox="0 0 8 8"><circle cx="4" cy="4" r="3.2" fill="none" stroke="#1fb5fa" stroke-width="1.3"/><path d="M4 2v2h1.6" stroke="#1fb5fa" stroke-width="1" fill="none"/></svg>Sat-Mon</div>
      <div><svg width="6" height="8" viewBox="0 0 6 8"><path d="M3 0a3 3 0 0 0-3 3c0 2 3 5 3 5s3-3 3-5a3 3 0 0 0-3-3z" fill="#1fb5fa"/></svg>18 Wexley Row, Hollinford</div>
      <div><svg width="7" height="7" viewBox="0 0 8 8"><path d="M1 1l2-.5 1 2-1 1a5 5 0 0 0 2 2l1-1 2 1-.5 2C3.5 7.5.5 4.5 1 1z" fill="#1fb5fa"/></svg>(555) 01 4620 377</div>
      <div><svg width="8" height="6" viewBox="0 0 8 6"><rect x=".5" y=".5" width="7" height="5" fill="none" stroke="#1fb5fa"/><path d="M.5.5L4 3.5 7.5.5" fill="none" stroke="#1fb5fa"/></svg>hello@thornfieldmarsh.example</div>
    </div>
    <div class="abs fcol" style="left:449px">
      <h4>PHOTO GALLERY</h4><div class="bar"></div>
      <div class="thumbs">
        <span class="t1" role="img" aria-label="Gallery photo: signing documents"></span>
        <span class="t2" role="img" aria-label="Gallery photo: scales of justice"></span>
        <span class="t3" role="img" aria-label="Gallery photo: courthouse columns"></span>
        <span class="t1" role="img" aria-label="Gallery photo: signing documents"></span>
        <span class="t2" role="img" aria-label="Gallery photo: scales of justice"></span>
        <span class="t3" role="img" aria-label="Gallery photo: courthouse columns"></span>
      </div>
    </div>
    <div class="abs fline"></div>
    <div class="abs totop"><svg width="13" height="13" viewBox="0 0 13 13"><path d="M4 8l2.5-2.5L9 8" fill="none" stroke="#000" stroke-width="1.3"/></svg></div>
    <p class="abs copy">Thornfield Marsh © All Rights Reserved</p>
  </footer>

</div>
</div>
</body>
</html>
```